Power Point for new apartment development

I need to create a power point that will help me present a new real estate development. I have put together the powerpoint without any graphics...just the highlights and included a bunch of pics attached to this post. Use them as needed when discussing each slide. I'm really looking to nail this. dont have much time so please work quick and i'll accept the second i like one.
Target Market(s)
investors and financing institutions
Industry/Entity Type
Real Estate
Font styles to use
Serif
Requirements
Must have
- just needs to be awesome... all your choice.
Nice to have
- nothing specific
Should not have
- nothing specific

```html
<!DOCTYPE html>
<html lang="en">
<head>
<meta charset="utf-8">
<title>The Harbor At Grand</title>
<link href="https://fonts.googleapis.com/css2?family=Source+Serif+4:opsz,wght@8..60,400;8..60,600;8..60,700&display=swap" rel="stylesheet">
<style>
  :root {
    --navy: #1d3a4c;
    --lime: #9dc92c;
    --ink: #333333;
    --rule: #d8d8d8;
    --glow: #f3f3f3;
    --paper: #ffffff;
  }
  * { margin: 0; padding: 0; box-sizing: border-box; }
  html, body { width: 1200px; height: 675px; overflow: hidden; background: var(--paper); }
  .slide {
    position: relative; width: 1200px; height: 675px; overflow: hidden;
    font-family: "Source Serif 4", Georgia, serif; color: var(--ink);
  }
  .backdrop {
    position: absolute; left: 150px; top: 110px; width: 564px; height: 564px;
    border-radius: 50%;
    background: radial-gradient(circle, var(--glow) 0%, rgba(243,243,243,0.6) 45%, rgba(255,255,255,0) 70%);
  }
  .header { position: absolute; left: 0; top: 0; width: 1200px; height: 98px; background: var(--navy); }
  .header-rule { position: absolute; left: 0; top: 98px; width: 1200px; height: 8px; background: var(--rule); }
  .title {
    position: absolute; right: 84px; top: 30px;
    font-size: 42px; line-height: 1; font-weight: 400; color: var(--lime); letter-spacing: -0.5px;
  }
  .block { position: absolute; }
  .stat-value, .feature-title { font-weight: 700; color: var(--lime); letter-spacing: -1px; }
  .stat { left: 68px; line-height: 1; }
  .stat-value { font-size: 56px; }
  .stat-value.word { font-size: 52px; }
  .stat-label { position: absolute; left: 68px; font-size: 16px; line-height: 1; }
  .feature { text-align: right; }
  .feature-title { font-size: 44px; line-height: 54px; }
  .feature-text { font-size: 15.5px; line-height: 22px; text-align: right; }
  .mid { right: 446px; }
  .side { right: 54px; }
  .side .feature-title { font-size: 48px; line-height: 54px; }
  .page-number { position: absolute; left: 1147px; top: 623px; font-size: 13px; font-weight: 700; }
</style>
</head>
<body>
<div class="slide">
  <div class="backdrop" role="img" aria-label="Soft grey circular backdrop glow"></div>

  <div class="header"></div>
  <div class="header-rule"></div>
  <h1 class="title">The Harbor At Grand</h1>

  <div class="block stat stat-value" style="top:137px">57</div>
  <div class="stat-label" style="top:210px">Apartment Units</div>
  <div class="block stat stat-value" style="top:258px">15</div>
  <div class="stat-label" style="top:334px">Boat Slips</div>
  <div class="block stat stat-value word" style="top:404px">Luxury</div>
  <div class="stat-label" style="top:466px">Apartment Homes</div>
  <div class="block stat stat-value" style="top:544px">30-40%</div>
  <div class="stat-label" style="top:614px">Smart Energy Management</div>

  <div class="block feature mid" style="top:129px">
    <div class="feature-title">Apartments</div>
  </div>
  <div class="block feature-text mid" style="top:192px">Manage and Control your entire apartment<br>home via mobile App or Online Web Portal</div>

  <div class="block feature mid" style="top:257px">
    <div class="feature-title">Milwaukee's<br>trendy &amp; active</div>
  </div>
  <div class="block feature-text" style="top:382px; right:440px">Located 3 Blocks or less , nightlife including;<br>N Milwaukee Street and Cathedral Square</div>

  <div class="block feature mid" style="top:447px">
    <div class="feature-title">Free Valet Parking</div>
  </div>
  <div class="block feature-text" style="top:509px; right:451px">Tips Absolutely Not Accepted</div>

  <div class="block feature mid" style="top:547px">
    <div class="feature-title">Health &amp; Fitness</div>
  </div>
  <div class="block feature-text mid" style="top:610px">Smart Facility</div>

  <div class="block feature side" style="top:127px">
    <div class="feature-title">Milwaukee's<br>Finest</div>
  </div>
  <div class="block feature-text side" style="top:261px; line-height:21px">Within 1 Block ,The Copper Grille, Vito's A<br>Place For Steaks, Riverbend Brewery,<br>Sakura House, The Hideout, Elm Tavern and<br>many others.</div>

  <div class="block feature side" style="top:353px">
    <div class="feature-title">Milwaukee<br>River</div>
  </div>
  <div class="block feature-text side" style="top:487px">Is at our Doorsteps, Directly in the Heart<br>as it flows through the downtown area</div>

  <div class="page-number">1</div>
</div>
</body>
</html>
```